Help! We need PROFESSIONAL E-mail Signatures that POP!

9/12 UPDATE:
We have extended the deadline.
Also the logo we want used for Melsford has changed.

We have 8 employees working for three companies. We want our e-mail signatures to be the same format and cohesive, but each person has one company of the three that needs to be highlighted.
- Logos are attached and spreadsheet shows what information is needed for each employee as well as which of the logos should be the primary logo - first one displayed and slightly larger than the others.
- Please create one design first using the information for Daniel Wystan from Line 2 of the spreadsheet (provided three versions - Numbers, Excel, PDF
- All components need to be able to be changed or deleted.
- We need to be able to easily create new signatures for new employees
Updates

Need extra days to review

If you submitted a design prior to yesterday afternoon, please see original brief for the updated Melsford logo. This is the version of the Melsford logo that will be used for all the email signatures. The spreadsheet with the info for all 8 employees show different versions of this logo for different employees. Ignore that. Use this one logo in the design along with the Pelna and Brisk logos as indicated on the spreadsheet. Thanks!

Target Market(s)

New/existing clients!

Industry/Entity Type

Property development, commercial construction, property management

Font styles to use
Sans Serif

Requirements
Must have
• A lot of info with a clean look
Nice to have
• Consistency and cohesion
Should not have
• Too many elements - UPDATE: No photos - thanks!

```html
<!DOCTYPE html>
<html lang="en">
<head>
<meta charset="utf-8">
<title>Email signatures – Melsford, Brisk, Pelna</title>
<link rel="stylesheet" href="https://fonts.googleapis.com/css2?family=Lexend:wght@300;400;500&display=swap">
<style>
  :root {
    --page: #eff0ef;
    --ink: #1b1b2f;
    --charcoal: #3d3d3f;
    --white: #ffffff;
    --green: #72cf45;
    --green-deep: #62c13a;
    --blue: #1474ba;
    --blue-deep: #2189d0;
    --orange: #f15a24;
    --orange-deep: #f0642c;
  }
  * { box-sizing: border-box; margin: 0; padding: 0; }
  html, body {
    width: 989px; height: 1200px; overflow: hidden;
    background: var(--page);
    font-family: "Lexend", sans-serif;
    color: var(--ink);
  }
  .sprite { position: absolute; width: 0; height: 0; }

  .signature {
    position: absolute; left: 83px; width: 823px; height: 275px;
    background: linear-gradient(90deg, var(--accent) 82%, var(--accent-deep));
    box-shadow: 0 2px 5px rgba(0,0,0,.18);
    overflow: hidden;
  }
  .signature--melsford { top: 111px; --accent: var(--green); --accent-deep: var(--green-deep); }
  .signature--brisk    { top: 465px; --accent: var(--blue);  --accent-deep: var(--blue-deep); }
  .signature--pelna    { top: 813px; --accent: var(--orange); --accent-deep: var(--orange-deep); }

  .signature__shape { position: absolute; inset: 0; width: 100%; height: 100%; }
  .signature__shape .paper { fill: var(--white); }
  .signature__shape .accent { fill: var(--accent); }

  /* Primary brand */
  .brand { position: absolute; display: flex; align-items: center; font-weight: 500; line-height: 1; }
  .brand__mark { display: block; flex: none; }
  .brand--melsford { left: 37px; top: 57px; gap: 10px; font-size: 33px; color: var(--charcoal); }
  .brand--melsford .brand__mark { width: 56px; height: 56px; background: var(--green); }
  .brand--brisk { left: 37px; top: 66px; gap: 12px; font-size: 62px; color: var(--blue); }
  .brand--brisk .brand__mark { width: 22px; height: 70px; background: var(--blue); }
  .brand--pelna { left: 37px; top: 58px; gap: 12px; font-size: 68px; color: var(--charcoal); }
  .brand--pelna .brand__mark { width: 26px; height: 26px; border-radius: 50%; background: var(--orange); }

  /* Person */
  .person { position: absolute; left: 37px; top: 184px; padding-left: 14px; border-left: 2px solid var(--accent); }
  .person__name { font-size: 28px; font-weight: 500; line-height: 1.05; letter-spacing: .3px; text-transform: uppercase; }
  .person__role { margin-top: 2px; font-size: 14.5px; font-weight: 300; letter-spacing: 3.2px; text-transform: uppercase; }
  .signature--pelna .person__role { letter-spacing: 1px; }

  /* Contact column */
  .contact { list-style: none; }
  .contact__item {
    position: absolute; left: 419px; display: flex; gap: 5px;
    font-size: 10.4px; line-height: 12.5px; color: var(--white);
  }
  .contact__icon { width: 18px; height: 18px; flex: none; margin-top: -2px; }
  .social { position: absolute; left: 444px; top: 203px; display: flex; gap: 5px; }
  .social__link {
    width: 25px; height: 25px; border-radius: 7px; background: var(--white);
    box-shadow: 0 2px 0 rgba(0,0,0,.15);
  }

  /* Other information column */
  .details { position: absolute; left: 591px; top: 43px; width: 209px; color: var(--white); }
  .details__title { font-size: 12px; font-weight: 300; margin-left: -2px; }
  .details__licence { margin-top: 5px; font-size: 10.2px; line-height: 12.5px; }
  .details__rule { border: 0; border-top: 1px solid rgba(255,255,255,.75); margin: 10px 0 0; }
  .details__notice-title { margin-top: 10px; font-size: 7.6px; font-weight: 400; }
  .details__notice { margin-top: 5px; font-size: 4.9px; line-height: 6.9px; font-weight: 400; }

  .partners { position: absolute; left: 591px; top: 190px; width: 210px; display: flex; justify-content: space-between; align-items: center; }
  .partner { display: flex; align-items: center; gap: 5px; font-weight: 500; line-height: 1; }
  .partner__mark { display: block; flex: none; }
  .partner--brisk { font-size: 22px; color: var(--blue); }
  .partner--brisk .partner__mark { width: 6px; height: 22px; background: var(--blue); }
  .partner--pelna { font-size: 26px; color: var(--charcoal); }
  .partner--melsford { font-size: 17px; color: var(--charcoal); }
  .partner--melsford .partner__mark { width: 27px; height: 27px; background: var(--white); }
  .signature--pelna .partner--melsford { color: var(--charcoal); }
</style>
</head>
<body>

<svg class="sprite" aria-hidden="true">
  <defs>
    <symbol id="icon-office" viewBox="0 0 20 20">
      <rect width="20" height="20" rx="4" fill="#3d3d3f"/>
      <rect x="5" y="4" width="8" height="12" fill="none" stroke="#fff" stroke-width="1.2"/>
      <path d="M7 7h4M7 9.5h4M7 12h4" stroke="#fff" stroke-width="1"/>
      <circle cx="14.5" cy="13.5" r="2.3" fill="#fff"/>
    </symbol>
    <symbol id="icon-phone" viewBox="0 0 20 20">
      <rect width="20" height="20" rx="4" fill="#3d3d3f"/>
      <path d="M6.2 4.5l2.3 2.6-1.3 1.6c.8 1.7 2.1 3 3.8 3.8l1.6-1.3 2.6 2.3-1.4 2c-4.6-.4-8.6-4.4-9-9z" fill="#fff"/>
    </symbol>
    <symbol id="icon-line" viewBox="0 0 20 20">
      <rect width="20" height="20" rx="4" fill="#3d3d3f"/>
      <rect x="4" y="5" width="12" height="10" rx="1" fill="none" stroke="#fff" stroke-width="1.2"/>
      <path d="M6.5 8h1.5M9.3 8h1.5M12 8h1.5M6.5 10.5h1.5M9.3 10.5h1.5M12 10.5h1.5M6.5 13h7" stroke="#fff" stroke-width="1.1"/>
    </symbol>
    <symbol id="icon-mail" viewBox="0 0 20 20">
      <rect width="20" height="20" rx="4" fill="#3d3d3f"/>
      <rect x="4" y="6" width="12" height="8.5" rx="1" fill="#fff"/>
      <path d="M4.5 6.6L10 11l5.5-4.4" fill="none" stroke="#3d3d3f" stroke-width="1"/>
    </symbol>
    <symbol id="icon-pin" viewBox="0 0 20 20">
      <rect width="20" height="20" rx="4" fill="#3d3d3f"/>
      <path d="M10 3.5a4 4 0 00-4 4c0 3 4 7 4 7s4-4 4-7a4 4 0 00-4-4z" fill="#fff"/>
      <circle cx="10" cy="7.6" r="1.5" fill="#3d3d3f"/>
      <ellipse cx="10" cy="15.6" rx="4.5" ry="1.2" fill="none" stroke="#fff" stroke-width="1"/>
    </symbol>
    <symbol id="icon-web" viewBox="0 0 20 20">
      <rect width="20" height="20" rx="4" fill="#3d3d3f"/>
      <circle cx="10" cy="10" r="5.5" fill="none" stroke="#fff" stroke-width="1.2"/>
      <ellipse cx="10" cy="10" rx="2.4" ry="5.5" fill="none" stroke="#fff" stroke-width="1"/>
      <path d="M4.5 10h11M5.3 7.3h9.4M5.3 12.7h9.4" stroke="#fff" stroke-width="1"/>
    </symbol>
  </defs>
</svg>

<!-- Melsford -->
<section class="signature signature--melsford">
  <svg class="signature__shape" viewBox="0 0 1445 482" preserveAspectRatio="none" aria-hidden="true">
    <polygon class="paper" points="0,0 474,0 775,452 0,478"/>
    <polygon class="accent" points="454,0 472,0 514,105"/>
    <polygon class="paper" points="614,482 1445,426 1445,434 770,482"/>
  </svg>

  <div class="brand brand--melsford"><span class="brand__mark"></span>Melsford</div>

  <div class="person">
    <p class="person__name">Daniel Wystan</p>
    <p class="person__role">CEO / Owner</p>
  </div>

  <ul class="contact">
    <li class="contact__item" style="top:42px"><svg class="contact__icon"><use href="#icon-office"/></svg><span>Melsford Pelna Brokerage &amp;<br>Management Brisk Builders</span></li>
    <li class="contact__item" style="top:76px"><svg class="contact__icon"><use href="#icon-phone"/></svg><span>555-201-4470</span></li>
    <li class="contact__item" style="top:98px"><svg class="contact__icon"><use href="#icon-line"/></svg><span>Melsford:<br>555-310-8820 x101</span></li>
    <li class="contact__item" style="top:132px"><svg class="contact__icon"><use href="#icon-mail"/></svg><span>dwystan@melsford.com</span></li>
    <li class="contact__item" style="top:152px"><svg class="contact__icon"><use href="#icon-pin"/></svg><span>112 N. Alder Ave.,<br>Ste 3B, Fairbrook IL 60999</span></li>
    <li class="contact__item" style="top:185px"><svg class="contact__icon"><use href="#icon-web"/></svg><span>www.melsford.com</span></li>
  </ul>
  <div class="social"><span class="social__link" aria-label="Social page"></span><span class="social__link" aria-label="Social page"></span></div>

  <div class="details">
    <p class="details__title">Other Information</p>
    <p class="details__licence">IL RE Lic#: 600.114872<br>Fairbrook GC Lic #: RGC051187</p>
    <hr class="details__rule">
    <p class="details__notice-title">CONFIDENTIALITY NOTICE:</p>
    <p class="details__notice">This e-mail is meant only for the recipient named and may hold private, protected material exempt from release under applicable law. If you are not the named recipient, you may have received this message in error. Please notify us at once by e-mail at operations@melsford.com and delete this message and all attached files from your system. Any sharing, copying, distribution or use of this message by others is prohibited and may expose you to liability.</p>
  </div>

  <div class="partners">
    <div class="partner partner--brisk"><span class="partner__mark"></span>Brisk</div>
    <div class="partner partner--pelna">Pelna</div>
  </div>
</section>

<!-- Brisk -->
<section class="signature signature--brisk">
  <svg class="signature__shape" viewBox="0 0 1445 482" preserveAspectRatio="none" aria-hidden="true">
    <polygon class="paper" points="0,0 474,0 775,452 0,478"/>
    <polygon class="accent" points="454,0 472,0 514,105"/>
    <polygon class="paper" points="614,482 1445,426 1445,434 770,482"/>
  </svg>

  <div class="brand brand--brisk"><span class="brand__mark"></span>Brisk</div>

  <div class="person">
    <p class="person__name">Lauren Hadley</p>
    <p class="person__role">Operations Manager</p>
  </div>

  <ul class="contact">
    <li class="contact__item" style="top:42px"><svg class="contact__icon"><use href="#icon-office"/></svg><span>Brisk Builders Melsford Pelna<br>Brokerage &amp; Management</span></li>
    <li class="contact__item" style="top:76px"><svg class="contact__icon"><use href="#icon-phone"/></svg><span>555-627-3309</span></li>
    <li class="contact__item" style="top:98px"><svg class="contact__icon"><use href="#icon-line"/></svg><span>Brisk Builders:<br>555-409-2216 x104</span></li>
    <li class="contact__item" style="top:132px"><svg class="contact__icon"><use href="#icon-mail"/></svg><span>operations@melsford.com</span></li>
    <li class="contact__item" style="top:152px"><svg class="contact__icon"><use href="#icon-pin"/></svg><span>112 N. Alder Ave.,<br>Ste 3B, Fairbrook IL 60999</span></li>
    <li class="contact__item" style="top:185px"><svg class="contact__icon"><use href="#icon-web"/></svg><span>www.builtbrisk.com</span></li>
  </ul>
  <div class="social"><span class="social__link" aria-label="Social page"></span><span class="social__link" aria-label="Social page"></span></div>

  <div class="details">
    <p class="details__title">Other Information</p>
    <p class="details__licence">Fairbrook GC Lic#: RGC051187</p>
    <hr class="details__rule">
    <p class="details__notice-title">CONFIDENTIALITY NOTICE:</p>
    <p class="details__notice">This e-mail is meant only for the recipient named and may hold private, protected material exempt from release under applicable law. If you are not the named recipient, you may have received this message in error. Please notify us at once by e-mail at operations@melsford.com and delete this message and all attached files from your system. Any sharing, copying, distribution or use of this message by others is prohibited and may expose you to liability.</p>
  </div>

  <div class="partners" style="top:198px">
    <div class="partner partner--melsford"><span class="partner__mark"></span>Melsford</div>
    <div class="partner partner--pelna">Pelna</div>
  </div>
</section>

<!-- Pelna -->
<section class="signature signature--pelna">
  <svg class="signature__shape" viewBox="0 0 1445 482" preserveAspectRatio="none" aria-hidden="true">
    <polygon class="paper" points="0,0 474,0 775,452 0,478"/>
    <polygon class="accent" points="454,0 472,0 514,105"/>
    <polygon class="paper" points="614,482 1445,426 1445,434 770,482"/>
  </svg>

  <div class="brand brand--pelna">Pelna<span class="brand__mark"></span></div>

  <div class="person">
    <p class="person__name">Rowan Ellery</p>
    <p class="person__role">Director of Commercial Real Estate</p>
  </div>

  <ul class="contact">
    <li class="contact__item" style="top:42px"><svg class="contact__icon"><use href="#icon-office"/></svg><span>Pelna Brokerage &amp;<br>Management Melsford</span></li>
    <li class="contact__item" style="top:76px"><svg class="contact__icon"><use href="#icon-phone"/></svg><span>555-914-6032</span></li>
    <li class="contact__item" style="top:98px"><svg class="contact__icon"><use href="#icon-line"/></svg><span>Pelna:<br>555-726-1185 x108</span></li>
    <li class="contact__item" style="top:132px"><svg class="contact__icon"><use href="#icon-mail"/></svg><span>rowan@melsford.com</span></li>
    <li class="contact__item" style="top:152px"><svg class="contact__icon"><use href="#icon-pin"/></svg><span>112 N. Alder Ave.,<br>Ste 3B, Fairbrook IL 60999</span></li>
    <li class="contact__item" style="top:185px"><svg class="contact__icon"><use href="#icon-web"/></svg><span>www.melsford.com</span></li>
  </ul>
  <div class="social"><span class="social__link" aria-label="Social page"></span><span class="social__link" aria-label="Social page"></span></div>

  <div class="details">
    <p class="details__title">Other Information</p>
    <p class="details__licence">IL RE Lic#: 612.338409<br>Fairbrook GC Lic#: RGC051187</p>
    <hr class="details__rule">
    <p class="details__notice-title">CONFIDENTIALITY NOTICE:</p>
    <p class="details__notice">This e-mail is meant only for the recipient named and may hold private, protected material exempt from release under applicable law. If you are not the named recipient, you may have received this message in error. Please notify us at once by e-mail at operations@melsford.com and delete this message and all attached files from your system. Any sharing, copying, distribution or use of this message by others is prohibited and may expose you to liability.</p>
  </div>

  <div class="partners" style="top:197px">
    <div class="partner partner--brisk"><span class="partner__mark"></span>Brisk</div>
    <div class="partner partner--melsford"><span class="partner__mark"></span>Melsford</div>
  </div>
</section>

</body>
</html>
```